teaching love. a joyful state of being.

adding value to ones circumstance through the teachings of neutralization. quote for back of card: "and then it happens... One day you wake up and you're in this place. You are in this place where everything is right. Your heart is calm. Your soul is lit. Your thoughts are positive. Your vision is clear. Your faith is stronger than ever. And you are at peace. At peace with where you have been. At peace with what you've been through. And at peace with where you're headed." -unknown

Target Market(s)

spiritual, awakening, inspiration, motivation, gratefulness, oneness, peace, positive mindset,

Contact Information for Business Card

front: one line message from quote

Logo Text

up to suggestions

Font styles to use
Serif
Sans Serif
Script

Colors

Designer to choose colors to be used in the design.

Requirements
Must have
• entire quote on one side of card
Nice to have
• simple, and to the point
Should not have
• elaborated designs

```html
<!DOCTYPE html>
<html lang="en">
<head>
<meta charset="UTF-8">
<title>And then it happens — quote card</title>
<link rel="stylesheet" href="https://fonts.googleapis.com/css2?family=Mulish:ital,wght@0,400;0,500;0,600;1,400&display=swap">
<style>
  :root {
    --page-bg: #d9d9d9;
    --card-bg: #1e1e1e;
    --card-edge: #2a2a2a;
    --ink: #f2f2f2;
    --ink-soft: #e4e4e4;
  }
  * { margin: 0; padding: 0; box-sizing: border-box; }
  html, body {
    width: 1200px;
    height: 1200px;
    overflow: hidden;
  }
  body {
    background: var(--page-bg);
    display: flex;
    align-items: center;
    justify-content: center;
    font-family: "Mulish", sans-serif;
  }
  .quote-card {
    width: 1000px;
    height: 572px;
    background: var(--card-bg);
    border: 1px solid var(--card-edge);
    display: flex;
    flex-direction: column;
    align-items: center;
    justify-content: center;
    text-align: center;
    color: var(--ink);
    padding: 40px 60px;
  }
  .quote-title {
    font-size: 44px;
    font-weight: 600;
    letter-spacing: 0.5px;
    margin-bottom: 10px;
  }
  .quote-body {
    font-size: 33px;
    font-weight: 500;
    line-height: 1.26;
    color: var(--ink-soft);
  }
  .quote-line { display: block; }
  .quote-source {
    font-size: 33px;
    font-style: italic;
    font-weight: 400;
    color: var(--ink-soft);
    margin-top: 2px;
  }
</style>
</head>
<body>
  <main class="quote-card">
    <h1 class="quote-title">And then it happens...</h1>
    <p class="quote-body">
      <span class="quote-line">One day you wake up and you're in this place.</span>
      <span class="quote-line">You are in this place where everything is right.</span>
      <span class="quote-line">Your heart is calm. Your soul is lit. Your thoughts</span>
      <span class="quote-line">are positive. Your vision is clear. Your faith is</span>
      <span class="quote-line">stronger than ever. And you are at peace. At</span>
      <span class="quote-line">peace with where you have been. At peace with</span>
      <span class="quote-line">what you've been through. And at peace with</span>
      <span class="quote-line">where you're headed.</span>
    </p>
    <p class="quote-source">- unknown</p>
  </main>
</body>
</html>
```